Real Estate Web Design

Hi

We are a real estate agency who is looking for a Corporate Design that would match our Style Guide. We have already developed the website but we want to apply our Branding on top of it. I am looking for some creative concepts

Below is our Test link for our new website
http://brightkeyhomes.sampledemo.com.au/

Attached is our Style Guide

Cheers
Ruvo

Industry/Entity Type

Real Estate

```html
<!DOCTYPE html>
<html lang="en">
<head>
<meta charset="utf-8">
<title>Brightkeyhomes – Real Estate</title>
<link href="https://fonts.googleapis.com/css2?family=Open+Sans:wght@400;600;700;800&display=swap" rel="stylesheet">
<style>
:root{
  --dark:#1d1d1d;
  --dark-2:#2a2a2a;
  --dark-3:#151515;
  --red:#d7262b;
  --blue:#1b6cae;
  --grey-bg:#ececec;
  --line:#d6d6d6;
  --text:#555;
  --muted:#8a8a8a;
  --white:#fff;
}
*{box-sizing:border-box;margin:0;padding:0}
html,body{width:885px;height:1200px;overflow:hidden}
body{font-family:"Open Sans",Arial,sans-serif;color:var(--text);background:var(--white);position:relative}

/* header */
.site-header{position:absolute;left:0;top:0;width:885px;height:96px;background:var(--dark)}
.brand{position:absolute;left:16px;top:22px;display:flex;align-items:center;gap:8px}
.brand-mark{width:40px;height:40px;background:var(--red)}
.brand-name{color:var(--white);font-weight:700;font-size:17px}
.date-line{position:absolute;left:16px;top:6px;font-size:8px;color:var(--muted)}
.top-contact{position:absolute;right:16px;top:8px;display:flex;gap:16px;font-size:9px;color:#ccc}
.top-contact span{display:flex;align-items:center;gap:4px}
.main-nav{position:absolute;left:250px;top:34px;display:flex}
.main-nav a{display:block;height:54px;line-height:54px;padding:0 17px;font-size:11px;font-weight:600;color:#ddd;text-decoration:none;border-left:1px solid #333}
.main-nav a.active{background:var(--red);color:var(--white)}

/* hero */
.hero{position:absolute;left:0;top:96px;width:885px;height:226px;background:#3a3a3a}
.hero-slide{position:absolute;left:16px;top:12px;width:574px;height:204px;background:linear-gradient(180deg,#9cc3e3 0%,#c9dbe8 45%,#a89478 62%,#5f7a45 100%)}
.slide-caption{position:absolute;left:16px;top:152px;width:300px;height:52px;background:rgba(0,0,0,.6);padding:7px 10px}
.slide-caption h2{font-size:13px;color:var(--white);font-weight:700}
.slide-caption p{font-size:8px;color:#ddd;line-height:11px}
.slide-price{position:absolute;left:530px;top:192px;width:60px;height:22px;background:var(--red);color:var(--white);font-size:11px;font-weight:700;text-align:center;line-height:22px}
.search-panel{position:absolute;left:600px;top:12px;width:270px;height:204px;background:#262626}
.search-panel h3{height:30px;line-height:30px;background:var(--red);color:var(--white);font-size:13px;text-align:center;font-weight:700}
.search-row{display:flex;align-items:center;margin:7px 14px 0;font-size:9px;color:#ccc}
.search-row label{width:70px}
.search-row .field{flex:1;height:17px;background:#f4f4f4;border:1px solid #999;font-size:8px;color:#888;padding-left:5px;line-height:15px}
.search-btn{position:absolute;right:14px;bottom:10px;width:58px;height:20px;background:var(--blue);color:var(--white);font-size:9px;font-weight:700;text-align:center;line-height:20px}

/* categories */
.categories{position:absolute;left:0;top:322px;width:885px;height:124px;background:var(--grey-bg);display:flex;justify-content:center;gap:40px;align-items:center}
.category{display:flex;align-items:center;gap:10px;width:200px}
.category-icon{width:76px;height:76px;border-radius:50%;background:var(--white);border:5px solid #d0d0d0;display:flex;align-items:center;justify-content:center}
.category small{display:block;font-size:8px;color:var(--muted);font-weight:600;letter-spacing:.5px}
.category strong{display:block;font-size:22px;color:#333;font-weight:800;line-height:24px}
.category em{font-style:normal;font-size:8px;color:var(--red)}

/* deals */
.section-title{font-size:19px;font-weight:700;color:var(--blue)}
.deals-title{position:absolute;top:462px;left:0;width:885px;text-align:center}
.deals-intro{position:absolute;top:492px;left:90px;width:705px;text-align:center;font-size:8px;line-height:12px;color:var(--muted)}
.card-row{position:absolute;left:20px;display:flex;gap:15px}
.deal-card{width:200px}
.photo{width:200px;height:112px}
.deal-card h4{font-size:10px;color:#333;font-weight:700;margin-top:6px}
.deal-card .price{font-size:10px;color:var(--red);font-weight:700}
.deal-card .meta{font-size:8px;color:var(--muted);border-top:1px solid var(--line);margin-top:3px;padding-top:3px}

/* featured */
.featured-title{position:absolute;left:20px;top:712px}
.featured-card{width:200px}
.featured-card h4{font-size:10px;color:#333;font-weight:700;margin-top:6px}
.featured-card p{font-size:8px;line-height:11px;color:var(--muted);margin-top:2px}
.more-btn{display:inline-block;margin-top:6px;background:var(--red);color:var(--white);font-size:8px;font-weight:700;padding:3px 10px}

/* testimonial */
.stories{position:absolute;left:20px;top:958px;width:845px;height:70px;border-top:1px solid var(--line);padding-top:12px;display:flex;gap:24px}
.stories-label{width:80px;font-size:11px;font-weight:700;color:#999;line-height:13px;font-style:italic}
.stories-label span{display:block;font-size:7px;font-style:normal;font-weight:400;color:var(--muted)}
.quote{flex:1;font-size:8px;line-height:11px;color:var(--muted);font-style:italic}

/* footer */
.site-footer{position:absolute;left:0;top:1040px;width:885px;height:140px;background:var(--dark-2);display:flex;padding:14px 20px 0;gap:20px}
.footer-col{width:196px}
.footer-col h5{font-size:11px;font-weight:700;color:var(--white);letter-spacing:.5px;margin-bottom:8px}
.footer-col li{list-style:none;font-size:8px;color:#bbb;line-height:14px}
.footer-col li::before{content:"›";color:var(--red);margin-right:5px;font-weight:700}
.gallery-grid{display:grid;grid-template-columns:repeat(3,44px);gap:5px}
.gallery-grid div{height:34px;background:linear-gradient(160deg,#8fb4d2,#6f8a58)}
.contact-line{display:flex;align-items:center;gap:6px;font-size:8px;color:#bbb;margin-bottom:7px}
.contact-line i{width:14px;height:14px;background:var(--red);display:flex;align-items:center;justify-content:center}
.copyright{position:absolute;left:0;top:1180px;width:885px;height:20px;background:var(--dark-3);color:#888;font-size:7px;text-align:center;line-height:20px}
</style>
</head>
<body>

<header class="site-header">
  <div class="date-line">Saturday, 12 May 2024</div>
  <div class="brand"><span class="brand-mark"></span><span class="brand-name">brightkeyhomes</span></div>
  <div class="top-contact">
    <span><svg width="9" height="9" viewBox="0 0 10 10"><path d="M2 1l2 2-1 1.5c.6 1.2 1.3 1.9 2.5 2.5L7 6l2 2-1.5 1.5C4.5 9 1 5.5.5 2.5z" fill="#d7262b"/></svg>08 - 5550 - 0142</span>
    <span><svg width="10" height="8" viewBox="0 0 10 8"><rect x=".5" y=".5" width="9" height="7" fill="none" stroke="#d7262b"/><path d="M.5.5l4.5 4 4.5-4" fill="none" stroke="#d7262b"/></svg>hello@brightkeyhomes.com.au</span>
  </div>
  <nav class="main-nav">
    <a class="active">Home</a><a>About Us</a><a>Land Leads</a><a>Tenants</a><a>Properties</a><a>Contact Us</a><a>Properties Opportunities</a>
  </nav>
</header>

<section class="hero">
  <div class="hero-slide" role="img" aria-label="Photo of a two-storey family house with a front lawn"></div>
  <div class="slide-caption">
    <h2>Fresh view House</h2>
    <p>14 Fernbrook Road, Hollow Park – four bedroom family home with garden.</p>
  </div>
  <div class="slide-price">$99000</div>
  <form class="search-panel">
    <h3>Find Your Home</h3>
    <div class="search-row"><label>Property</label><div class="field">Select Type</div></div>
    <div class="search-row"><label>Price</label><div class="field">Select Price</div></div>
    <div class="search-row"><label>Region</label><div class="field">Select Region</div></div>
    <div class="search-row"><label>Rooms</label><div class="field">Select Rooms</div></div>
    <div class="search-row"><label>Keyword</label><div class="field"></div></div>
    <div class="search-btn">Search</div>
  </form>
</section>

<section class="categories">
  <div class="category">
    <div class="category-icon"><svg width="34" height="30" viewBox="0 0 34 30"><path d="M3 15L17 3l14 12M7 12v15h20V12" fill="none" stroke="#555" stroke-width="2.5"/><rect x="14" y="18" width="6" height="9" fill="#d7262b"/></svg></div>
    <div><small>PROPERTIES FOR</small><strong>SALE</strong><em>View all Properties &gt;&gt;</em></div>
  </div>
  <div class="category">
    <div class="category-icon"><svg width="34" height="30" viewBox="0 0 34 30"><path d="M3 15L17 3l14 12M7 12v15h20V12" fill="none" stroke="#555" stroke-width="2.5"/><circle cx="17" cy="19" r="3.5" fill="#d7262b"/></svg></div>
    <div><small>PROPERTIES FOR</small><strong>RENT</strong><em>View all Properties &gt;&gt;</em></div>
  </div>
  <div class="category">
    <div class="category-icon"><svg width="34" height="30" viewBox="0 0 34 30"><path d="M3 15L17 3l14 12M7 12v15h20V12" fill="none" stroke="#555" stroke-width="2.5"/><path d="M13 19l3 3 6-6" fill="none" stroke="#d7262b" stroke-width="2.5"/></svg></div>
    <div><small>PROPERTIES FOR</small><strong>LEASE</strong><em>View all Properties &gt;&gt;</em></div>
  </div>
</section>

<h2 class="section-title deals-title">We are Offering the Best Real Estate Deals</h2>
<p class="deals-intro">For the past 15 years in the North West we have been helping local families find the right home. Our team provides honest advice on buying, selling and renting, and we know every street in the area. Browse the latest listings below or contact our office to arrange a private inspection at a time that suits you.</p>

<div class="card-row" style="top:528px">
  <article class="deal-card">
    <div class="photo" role="img" aria-label="Photo of a brick house with a garage" style="background:linear-gradient(180deg,#a9c8e2,#b29a7c 60%,#6e8450)"></div>
    <h4>8 Linden Road, Hollow Park</h4><div class="price">$375 Week</div><div class="meta">3 Beds | 2 Baths | 2 Cars</div>
  </article>
  <article class="deal-card">
    <div class="photo" role="img" aria-label="Photo of a modern living room" style="background:linear-gradient(160deg,#e2d8c8,#a88f70 60%,#5e4c3a)"></div>
    <h4>14 Fernbrook Road, WA 6090</h4><div class="price">$420 Week</div><div class="meta">4 Beds | 2 Baths | 2 Cars</div>
  </article>
  <article class="deal-card">
    <div class="photo" role="img" aria-label="Photo of a bright kitchen interior" style="background:linear-gradient(160deg,#f0ece4,#c7b9a3 55%,#7d6a55)"></div>
    <h4>3 Millstone Crescent, WA 6090</h4><div class="price">$399 Week</div><div class="meta">3 Beds | 1 Bath | 1 Car</div>
  </article>
  <article class="deal-card">
    <div class="photo" role="img" aria-label="Photo of a white suburban house" style="background:linear-gradient(180deg,#9fc2df,#d8d6cf 55%,#6d8750)"></div>
    <h4>22B Banksia Street, Hollow Park</h4><div class="price">$350 Week</div><div class="meta">3 Beds | 2 Baths | 1 Car</div>
  </article>
</div>

<h2 class="section-title featured-title">Featured Properties</h2>
<div class="card-row" style="top:746px">
  <article class="featured-card">
    <div class="photo" role="img" aria-label="Photo of a family house with a porch" style="background:linear-gradient(180deg,#a4c6e1,#a58b6c 58%,#5f7a45)"></div>
    <h4>Estate villa Large Street</h4><p>Four bedroom home on a large block close to schools, shops and the local park.</p><span class="more-btn">More</span>
  </article>
  <article class="featured-card">
    <div class="photo" role="img" aria-label="Photo of a townhouse at dusk" style="background:linear-gradient(180deg,#8fb2d6,#c9b59b 58%,#6a7e4c)"></div>
    <h4>16 Westleigh Road, Hollow Park</h4><p>Neat family home with open living areas, a new kitchen and a shaded yard.</p><span class="more-btn">More</span>
  </article>
  <article class="featured-card">
    <div class="photo" role="img" aria-label="Photo of a house with a sunset sky" style="background:linear-gradient(180deg,#e6a25e,#8b6a50 58%,#3f4a30)"></div>
    <h4>Unit 7/48 Riverside Boulevard</h4><p>Spacious apartment with river views, secure parking and a quiet outlook.</p><span class="more-btn">More</span>
  </article>
  <article class="featured-card">
    <div class="photo" role="img" aria-label="Photo of a large two-storey home" style="background:linear-gradient(180deg,#a9cbe6,#cfc3b0 55%,#64804a)"></div>
    <h4>20 Wattle Street, Glenmore</h4><p>Classic residence with formal lounge, study and a generous rear garden.</p><span class="more-btn">More</span>
  </article>
</div>

<section class="stories">
  <div class="stories-label">SUCCESS STORY<span>What our clients say</span></div>
  <p class="quote">“The team made selling our home simple. They kept us informed at every step and found the right buyer within weeks. We would happily recommend them to friends and family.”</p>
  <p class="quote">“Finding a rental felt easy with their help. Friendly staff, quick replies and a great choice of properties. We moved into our new place sooner than we hoped.”</p>
</section>

<footer class="site-footer">
  <div class="footer-col">
    <h5>PROPERTIES</h5>
    <ul><li>Properties for Sale</li><li>Apartments for Rent</li><li>Office Spaces</li><li>Recent Houses</li><li>Land for Lease</li><li>Latest offers</li></ul>
  </div>
  <div class="footer-col">
    <h5>ABOUT US</h5>
    <ul><li>Why Work Together</li><li>Our Experience</li><li>Our Expertise</li><li>Our Location</li><li>Get in touch</li></ul>
  </div>
  <div class="footer-col">
    <h5>GALLERY</h5>
    <div class="gallery-grid" role="img" aria-label="Thumbnails of property photos">
      <div></div><div></div><div></div><div></div><div></div><div></div>
    </div>
  </div>
  <div class="footer-col">
    <h5>CONTACT US</h5>
    <div class="contact-line"><i><svg width="8" height="8" viewBox="0 0 10 10"><path d="M2 1l2 2-1 1.5c.6 1.2 1.3 1.9 2.5 2.5L7 6l2 2-1.5 1.5C4.5 9 1 5.5.5 2.5z" fill="#fff"/></svg></i>08 - 5550 - 0142</div>
    <div class="contact-line"><i><svg width="9" height="7" viewBox="0 0 10 8"><rect x=".5" y=".5" width="9" height="7" fill="none" stroke="#fff"/><path d="M.5.5l4.5 4 4.5-4" fill="none" stroke="#fff"/></svg></i>hello@brightkeyhomes.com.au</div>
    <div class="contact-line"><i><svg width="7" height="9" viewBox="0 0 8 10"><path d="M4 10S0 5.5 0 3.8a4 4 0 018 0C8 5.5 4 10 4 10z" fill="#fff"/></svg></i>100 Harbour Lane, Hollow Park WA 6090</div>
  </div>
</footer>
<div class="copyright">Copyright © 2024 brightkeyhomes. All Rights Reserved.</div>

</body>
</html>
```